Dog care service needs advertising poster

Our company is Paw Haven. We provide care for dogs while their owners are away, either through home visits or a holiday stay in the homes of carefully selected minders. Our existing website & Facebook cover should provide all the colour cues for a poster - namely blues, blondes and grey. We have an existing logo (provided). We can feature the same imagery from our website as I have purchased the rights to the stock images.

www.pawhavenexample.com.au
www.facebook.com/pawhavenexampleau

This brief is for design of a poster that can be placed in vet surgeries, groomers, on community noticeboards. It should be scalable to print in three sizes, A5, A4 & A3.

We wish to clearly communicate our three areas of service "dog minding, home visits, dog walking".

We would like to have the files ready for upload to Printora (or similar) for immediate printing.

Target Market(s)

Dog owners who love their dogs like family.

Industry/Entity Type

Advertising

Font styles to use
Sans Serif

Colors
33a6d7
3276b5

Requirements
Must have
• Logo
• www.pawhavenexample.com.au
• Telephone number
• Three services - Dog Minding, Home Visits, Dog Walking
Nice to have
• use of our existing stock photography to highlight the three areas of service - Dog minding, home visits, dog walking. Existing colour palette - blues, blondes and grey.
• Text that can be used:
• Western Sydney’s complete dog care service.
• Dog Minding - Your dog stays in the home of one of our carefully selected minders.Treated like part of the family, they enjoy all the creature comforts they are used to.
• Home Visits - We visit your dog at your home for feeding, walking and playtime. Short of long visits available.
• Dog Walking - If you can't walk your dog for any reason we are here to help. 1/2 hour or hourly walks available.
• Contact us today for a tailored package to meet your needs.
Should not have
• Any additional illustrations beyond the logo.

```html
<!DOCTYPE html>
<html lang="en">
<head>
<meta charset="utf-8">
<title>Paw Haven – Dog Care Poster</title>
<link rel="stylesheet" href="https://fonts.googleapis.com/css2?family=Ubuntu:wght@500;700&family=Questrial&family=Exo+2:ital,wght@1,500&display=swap">
<style>
  :root {
    --ink: #3b4350;
    --ink-soft: #4a5260;
    --paper: #f1f2f4;
    --sky: #33a6d7;
    --ocean: #3276b5;
    --ring: #4cc3e0;
    --white: #ffffff;
  }
  * { box-sizing: border-box; margin: 0; padding: 0; }
  html, body { width: 1200px; height: 879px; overflow: hidden; background: #e4e4e4; }
  .poster {
    position: relative; width: 1200px; height: 879px; overflow: hidden;
    background: var(--paper); color: var(--ink);
    font-family: "Questrial", sans-serif;
  }
  .backdrop { position: absolute; inset: 0; }

  .brand { position: absolute; left: 46px; top: 64px; display: flex; align-items: center; gap: 30px; }
  .brand-mark { width: 118px; height: 118px; border-radius: 50%; background: var(--ocean); }
  .brand-name { font-family: "Ubuntu", sans-serif; font-weight: 500; font-size: 50px; line-height: 46px; color: var(--ink); }
  .brand-tag { font-family: "Ubuntu", sans-serif; font-weight: 500; font-size: 17px; letter-spacing: 6px; color: var(--ocean); margin-top: 14px; padding-left: 46px; }

  .service-photo {
    position: absolute; width: 194px; height: 194px; border-radius: 50%;
    border: 3px solid var(--ring); padding: 5px; background: var(--white);
  }
  .service-photo span { display: block; width: 100%; height: 100%; border-radius: 50%; }
  .photo-minding { left: 556px; top: 32px; }
  .photo-minding span { background: linear-gradient(160deg, #8fb4d6, #6d7b62 55%, #7fae4a); }
  .photo-visits { left: 760px; top: 32px; }
  .photo-visits span { background: linear-gradient(180deg, #ece8e1 45%, #8a5a34); }
  .photo-walking { left: 968px; top: 30px; }
  .photo-walking span { background: linear-gradient(180deg, #4a6a3a, #86b653); }

  .headline {
    position: absolute; left: 32px; top: 249px;
    font-family: "Ubuntu", sans-serif; font-weight: 700; font-size: 34px; color: var(--ink);
  }

  .services { position: absolute; left: 34px; top: 314px; list-style: none; }
  .service { display: flex; margin-bottom: 24px; }
  .service-name {
    flex: 0 0 185px; position: relative; padding-left: 22px;
    font-family: "Ubuntu", sans-serif; font-weight: 700; font-size: 24px; color: var(--ink);
  }
  .service-name::before {
    content: ""; position: absolute; left: 0; top: 10px; width: 15px; height: 15px; border-radius: 50%;
    background: radial-gradient(circle at 35% 35%, #bfe6f6, var(--ocean));
  }
  .service-text { font-size: 21.5px; line-height: 25px; color: var(--ink-soft); width: 515px; }
  .service-text.narrow { width: 435px; }

  .call-to-action {
    position: absolute; left: 32px; top: 582px;
    font-family: "Ubuntu", sans-serif; font-weight: 700; font-size: 29px; line-height: 37px; color: var(--ink);
  }

  .phone { position: absolute; left: 36px; top: 812px; display: flex; align-items: center; gap: 8px;
    font-family: "Ubuntu", sans-serif; font-weight: 500; font-size: 41px; color: var(--ink); }
  .contact { position: absolute; left: 352px; top: 746px; list-style: none; font-family: "Ubuntu", sans-serif; font-weight: 500; font-size: 17px; color: var(--ink); }
  .contact li { display: flex; align-items: flex-start; gap: 6px; line-height: 28px; margin-bottom: 3px; }
  .contact svg { flex: 0 0 auto; margin-top: 6px; }

  .promise { position: absolute; right: 40px; top: 770px; text-align: right; color: var(--white);
    font-family: "Exo 2", sans-serif; font-style: italic; font-weight: 500; }
  .promise-years { font-size: 32px; line-height: 40px; }
  .promise-family { font-size: 27px; line-height: 48px; }
</style>
</head>
<body>
<main class="poster">
  <svg class="backdrop" width="1200" height="879" viewBox="0 0 1200 879" aria-hidden="true">
    <defs>
      <linearGradient id="scene-base" x1="0" y1="1" x2="1" y2="0">
        <stop offset="0" stop-color="#aaa69e"/>
        <stop offset="0.45" stop-color="#8e96a0"/>
        <stop offset="0.75" stop-color="#4f6a8c"/>
        <stop offset="1" stop-color="#1f2935"/>
      </linearGradient>
      <radialGradient id="scene-glow" cx="1000" cy="560" r="300" gradientUnits="userSpaceOnUse">
        <stop offset="0" stop-color="#d9a75c" stop-opacity="0.95"/>
        <stop offset="0.55" stop-color="#c9975a" stop-opacity="0.6"/>
        <stop offset="1" stop-color="#c9975a" stop-opacity="0"/>
      </radialGradient>
    </defs>
    <g role="img" aria-label="Photo: a golden puppy leaning out of a blue car window on a roadside">
      <path d="M1020,0 C920,230 840,420 712,520 C560,640 300,722 0,728 L0,879 L1200,879 L1200,0 Z" fill="url(#scene-base)"/>
      <path d="M1020,0 C920,230 840,420 712,520 C560,640 300,722 0,728 L0,879 L1200,879 L1200,0 Z" fill="url(#scene-glow)"/>
    </g>
    <path d="M1020,0 C920,230 840,420 712,520" fill="none" stroke="var(--ocean)" stroke-width="7"/>
    <path d="M0,716 C300,712 560,640 720,512 C610,660 330,770 0,780 Z" fill="var(--sky)"/>
    <path d="M0,780 C330,770 610,660 720,512 C630,672 360,800 0,806 Z" fill="var(--white)"/>
  </svg>

  <header class="brand">
    <div class="brand-mark"></div>
    <div>
      <div class="brand-name">Paw<br>Haven</div>
      <div class="brand-tag">PET SERVICES</div>
    </div>
  </header>

  <div class="service-photo photo-minding"><span role="img" aria-label="Photo: a shepherd dog lying in green grass"></span></div>
  <div class="service-photo photo-visits"><span role="img" aria-label="Photo: a small terrier sitting on a home doormat"></span></div>
  <div class="service-photo photo-walking"><span role="img" aria-label="Photo: a bulldog on a lead standing on a lawn"></span></div>

  <h1 class="headline">Western Sydney’s complete dog care service.</h1>

  <ul class="services">
    <li class="service">
      <span class="service-name">Dog Minding:</span>
      <p class="service-text">Your dog stays in the home of one of our carefully selected minders. Treated like part of the family, they enjoy all the creature comforts they are used to.</p>
    </li>
    <li class="service">
      <span class="service-name">Home Visits:</span>
      <p class="service-text">We visit your dog at your home for feeding, walking and playtime. Short of long visits available.</p>
    </li>
    <li class="service">
      <span class="service-name">Dog Walking:</span>
      <p class="service-text narrow">If you can't walk your dog for any reason we are here to help. 1/2 hour or hourly walks available.</p>
    </li>
  </ul>

  <p class="call-to-action">Contact us today for<br>a tailored package<br>to meet your needs.</p>

  <div class="phone">
    <svg width="22" height="38" viewBox="0 0 22 38" aria-hidden="true">
      <rect x="2" y="6" width="18" height="30" rx="3" fill="none" stroke="var(--ink)" stroke-width="3"/>
      <rect x="5" y="0" width="3" height="8" fill="var(--ink)"/>
      <rect x="6" y="11" width="10" height="7" fill="var(--ink)"/>
      <g fill="var(--ink)"><rect x="6" y="22" width="3" height="3"/><rect x="13" y="22" width="3" height="3"/><rect x="6" y="28" width="3" height="3"/><rect x="13" y="28" width="3" height="3"/></g>
    </svg>
    <span>0400 000 123</span>
  </div>

  <ul class="contact">
    <li>
      <svg width="12" height="17" viewBox="0 0 12 17" aria-hidden="true"><path d="M6,0 C2.7,0 0,2.6 0,5.8 C0,10 6,17 6,17 C6,17 12,10 12,5.8 C12,2.6 9.3,0 6,0 Z" fill="var(--ink)"/><circle cx="6" cy="5.8" r="2.3" fill="#aaa69e"/></svg>
      <span>Greenvale Park, New South Wales,<br>Australia 2999</span>
    </li>
    <li>
      <svg width="22" height="15" viewBox="0 0 22 15" aria-hidden="true"><rect x="1" y="1" width="20" height="13" fill="none" stroke="var(--ink)" stroke-width="2"/><path d="M1,1 L11,9 L21,1" fill="none" stroke="var(--ink)" stroke-width="2"/></svg>
      <span>info@pawhavenexample.com.au</span>
    </li>
    <li>
      <svg width="18" height="18" viewBox="0 0 18 18" aria-hidden="true"><g fill="none" stroke="var(--ink)" stroke-width="1.6"><circle cx="9" cy="9" r="8"/><ellipse cx="9" cy="9" rx="3.6" ry="8"/><path d="M1,9 H17 M2.5,5 H15.5 M2.5,13 H15.5"/></g></svg>
      <span>www.pawhavenexample.com.au</span>
    </li>
  </ul>

  <div class="promise">
    <p class="promise-years">Over 20 years’ experience</p>
    <p class="promise-family">Caring for your dog like family</p>
  </div>
</main>
</body>
</html>
```